VEXO requires an exciting new business card

New business card required for VEXO. We are a new market research consultancy and want our brand to be approachable and be contemporary/modern, bold, uncomplicated/simple, and use friendly and easy to read fonts.

A draft website front page is attached to give you a feel (the pictures will be improved over the coming days).

The business card will be printed on 600gsm card, full colour both sides. The card is unique in that it allows one of four colours to be placed within the seam of the card (see http://uk.tarnix.com/products/halo/business-cards.html)

The logo has been designed in yellow on white, white on yellow, yellow on black and black on yellow - please select whichever you feel most appropriate from the attached document (please use the versions with the tagline). I think my preference is yellow on white for the front, and then yellow or black as the dominant colour on the back.

Telephone numbers will be given next week as they are now being finalised.

Thanks

Target Market(s)

Professionals in large corporates, such as Marketing Managers at Bravik, Fizzor Dune, Domacore etc.

Industry/Entity Type

Market Research

Requirements
Must have
• Greg Hallow QPMR
vexo
Level 4, 17 Ember St
Quindle Park
NSW 2087
Tel: 02 XXXX XXXX
Mob: XXXX XXXXXX
Email: greg@vexomr.com.au
Web: www.vexomr.com.au

```html
<!DOCTYPE html>
<html lang="en">
<head>
<meta charset="utf-8">
<title>VEXO Business Card</title>
<link rel="stylesheet" href="https://fonts.googleapis.com/css2?family=PT+Sans:ital,wght@0,400;0,700;1,400&display=swap">
<style>
  :root {
    --brand-yellow: #ffcc00;
    --ink: #3f3f3f;
    --band-dark: #444444;
    --paper: #ffffff;
    --page: #ffffff;
    --card-shadow: rgba(0, 0, 0, 0.28);
  }
  * { box-sizing: border-box; margin: 0; padding: 0; }
  html, body {
    width: 1200px;
    height: 900px;
    overflow: hidden;
    background: var(--page);
    font-family: "PT Sans", Arial, sans-serif;
    color: var(--ink);
  }
  .canvas {
    position: relative;
    width: 1200px;
    height: 900px;
  }
  .card {
    position: absolute;
    width: 578px;
    height: 388px;
    background: var(--paper);
    box-shadow: 2px 3px 8px var(--card-shadow);
    overflow: hidden;
  }
  /* Front */
  .card--front { left: 79px; top: 54px; }
  .front-lockup {
    position: absolute;
    left: 74px;
    top: 118px;
  }
  .brand-name {
    display: block;
    font-weight: 700;
    color: var(--ink);
    line-height: 1;
  }
  .brand-name--large {
    font-size: 112px;
    letter-spacing: 4px;
  }
  .tagline {
    margin-top: 10px;
    margin-left: 6px;
    font-size: 27px;
    color: var(--ink);
  }
  /* Back */
  .card--back { left: 545px; top: 461px; }
  .name-band {
    height: 94px;
    background: var(--brand-yellow);
    padding: 46px 0 0 35px;
  }
  .name {
    font-size: 30px;
    font-weight: 400;
    line-height: 36px;
    color: var(--ink);
    letter-spacing: -0.5px;
  }
  .details { padding: 4px 0 0 35px; }
  .title-row {
    display: flex;
    align-items: baseline;
    gap: 12px;
    height: 36px;
    padding-top: 4px;
  }
  .qualification { font-size: 22px; font-weight: 700; color: var(--ink); }
  .brand-name--small { display: inline; font-size: 22px; letter-spacing: 1px; }
  .address {
    font-style: italic;
    font-size: 21px;
    line-height: 27px;
    margin-top: 4px;
    letter-spacing: -0.4px;
  }
  .phones {
    font-size: 25px;
    line-height: 32px;
    margin-top: 12px;
    letter-spacing: -0.4px;
  }
  .web-band {
    position: absolute;
    left: 0;
    bottom: 0;
    width: 100%;
    height: 62px;
    background: var(--band-dark);
    color: var(--paper);
    padding: 10px 0 0 35px;
    font-size: 15px;
    line-height: 20px;
    font-weight: 700;
    letter-spacing: -0.3px;
  }
</style>
</head>
<body>
  <main class="canvas">
    <section class="card card--front" aria-label="Card front">
      <div class="front-lockup">
        <span class="brand-name brand-name--large">VEXO</span>
        <p class="tagline">progressive research</p>
      </div>
    </section>

    <section class="card card--back" aria-label="Card back">
      <header class="name-band">
        <h1 class="name">Greg Hallow</h1>
      </header>
      <div class="details">
        <div class="title-row">
          <span class="qualification">QPMR</span>
          <span class="brand-name brand-name--small">VEXO</span>
        </div>
        <address class="address">
          Level 4, 17 Ember St<br>
          Quindle Park<br>
          NSW 2087
        </address>
        <p class="phones">
          Tel : 02 XXXX XXXX<br>
          Mob : XXXX XXXXXX
        </p>
      </div>
      <footer class="web-band">
        Email: greg@vexomr.com.au<br>
        Web: www.vexomr.com.au
      </footer>
    </section>
  </main>
</body>
</html>
```